Please look at my website to get a better understanding of my business: www.perovatu.com
This business is about Life Coaching for Families, couples, teenagers and individuals. I work more w parents of teenagers (as well as teenagers) but not so much with young kids.
The card should be fun, not too busy, with a sense of flow and playfulness. Warm colors, artistic style (can have a family sculpture, paining or a picture in it). Basic information about myself and my company

Reason: I extended my due date for next Tuesday, November 13th. Please summit new designs if you haven't done so, and for those who submitted, thank you so much for your time and effort. I will make a decision next Tues, and will contact you if I need to revise some items. Much thanks to you all! Orla

Families, parents, teenagers, couples, individuals.

Business

• Business name: PeRoVaTu! Hearth Circle Life Coaching
My name: Orla Bekwith, RMTQ
Description of my work: Tri-Mode life coach
Tel: 555-304-7719
Website: www.PeRoVaTu.com
• Family sculpture, abstract painting or a picture, or simply a nice background w/out a picture added.
• Corporate feeling, cold colors, corporate symbols. no Sunset, or picture of families on the beach.
Don't include bar-code (from uploaded file 1, it is only the designer to find out more about my website).

```html
<!DOCTYPE html>
<html lang="en">
<head>
<meta charset="utf-8">
<title>PeRoVaTu – Hearth Circle Life Coaching business cards</title>
<link rel="stylesheet" href="https://fonts.googleapis.com/css2?family=Bodoni+Moda:wght@500&family=Source+Sans+3:wght@400;600;700&display=swap">
<style>
  :root {
    --stage: #1f2626;
    --brown: #5a3219;
    --ink: #111111;
    --ink-soft: #333333;
    --lavender: #d9cde6;
    --lilac: #c9b8dc;
    --peach: #f1d2c2;
    --cream: #f7efe0;
    --white: #fbf9fc;
  }
  html, body {
    margin: 0;
    padding: 0;
    width: 976px;
    height: 1200px;
    overflow: hidden;
    background: var(--stage);
  }
  .canvas {
    position: relative;
    width: 976px;
    height: 1200px;
  }
  .card {
    position: absolute;
    left: 79px;
    width: 819px;
    height: 468px;
    border-radius: 24px;
    overflow: hidden;
    text-align: center;
  }
  .card--front { top: 107px; }
  .card--back { top: 654px; }
  .card__art {
    position: absolute;
    inset: 0;
    background:
      radial-gradient(ellipse 30% 35% at 58% 42%, var(--white) 0%, rgba(251,249,252,0) 100%),
      radial-gradient(ellipse 40% 40% at 85% 30%, var(--peach) 0%, rgba(241,210,194,0) 100%),
      radial-gradient(ellipse 45% 40% at 10% 85%, var(--peach) 0%, rgba(241,210,194,0) 100%),
      radial-gradient(ellipse 40% 40% at 20% 20%, var(--cream) 0%, rgba(247,239,224,0) 100%),
      linear-gradient(135deg, var(--lavender) 0%, var(--lilac) 50%, var(--lavender) 100%);
  }
  .line {
    position: absolute;
    left: 0;
    right: 0;
    margin: 0;
    line-height: 1;
  }
  .brand {
    font-family: "Source Sans 3", sans-serif;
    font-weight: 600;
    color: var(--brown);
  }
  .tagline {
    font-family: "Bodoni Moda", serif;
    font-weight: 500;
    color: var(--brown);
  }
  .sans {
    font-family: "Source Sans 3", sans-serif;
    color: var(--ink);
  }
  .card--front .brand { top: 72px; font-size: 82px; }
  .card--front .tagline { top: 186px; font-size: 33px; }
  .role { top: 272px; font-size: 27px; font-weight: 700; }
  .name { top: 328px; font-size: 21px; font-weight: 700; }
  .name__cred { font-size: 15px; font-weight: 400; }
  .contact { top: 375px; font-size: 21px; }
  .contact__key { font-weight: 700; font-style: italic; }
  .contact__sep { padding: 0 8px; }
  .address { top: 423px; font-size: 23px; }
  .card--back .brand { top: 110px; font-size: 96px; }
  .card--back .tagline { top: 268px; font-size: 38px; }
  .card--back .site { top: 394px; font-size: 28px; color: var(--ink-soft); }
</style>
</head>
<body>
<main class="canvas">
  <section class="card card--front">
    <div class="card__art" role="img" aria-label="Soft abstract marbled painting in lavender, peach and cream"></div>
    <p class="line brand">PeRoVaTu</p>
    <p class="line tagline">Hearth Circle Life Coaching</p>
    <p class="line sans role">Tri-Mode life coach</p>
    <p class="line sans name">Orla Bekwith, <span class="name__cred">RMTQ</span></p>
    <p class="line sans contact"><span class="contact__key">t</span> : 555-304-7719<span class="contact__sep">|</span><span class="contact__key">w</span> : www.PeRoVaTu.com</p>
    <p class="line sans address">Street Name, Area Name, City, Country Code.</p>
  </section>
  <section class="card card--back">
    <div class="card__art" role="img" aria-label="Soft abstract marbled painting in lavender, peach and cream"></div>
    <p class="line brand">PeRoVaTu</p>
    <p class="line tagline">Hearth Circle Life Coaching</p>
    <p class="line sans site">www.PeRoVaTu.com</p>
  </section>
</main>
</body>
</html>
```